Design a styled business card for an intimacy and attachment psychologist

I am a Psychologist providing online therapy to patients across the United States. My work is interpersonal and emotion-focused, with an emphasis on the client-therapist relationship. My primary areas of work are very personal, including sexuality and gender, abuse and trauma, and grief and loss. My target audience will be adults of all ages 18+.
My business card should convey a warm and inviting feeling of professionalism that is also casual and comfortable.
The front should be fairly simple and professional, consisting of:
- My name, Dr. Rosalind Petrakis
- My title, Licensed Psycholigist
- My logo
On either the front or the back, my contact information should be listed:
- ros@drrospetrakis.example
- 555.014.7788
- drrospetrakis.example
On the rear, I would like a description of the areas that I specialize in. This can be formatted in any way that appears stylistically interesting.
Individual and Couples
Relationships and Infidelity
Sexual Health & Aging
Gender Identity & Sexual Orientation
Abuse and Trauma
Sexual Compulsivity & Addiction
Sexual Dysfunction
Target Market(s)
My target audience will be adults of all ages 18+.
Industry/Entity Type
Psychology
Contact Information for Business Card
The front should be fairly simple and professional, consisting of: - My name, Dr. Rosalind Petrakis - My title, Licensed Psycholigist - My logo On either the front or the back, my contact information should be listed: - ros@drrospetrakis.example - 555.014.7788 - drrospetrakis.example On the rear, I would like a description of the areas that I specialize in. This can be formatted in any way that appears stylistically interesting. Individual and Couples Relationships and Infidelity Sexual Health & Aging Gender Identity & Sexual Orientation Abuse and Trauma Sexual Compulsivity & Addiction Sexual Dysfunction
- Follow brand guide

```html
<!DOCTYPE html>
<html lang="en">
<head>
<meta charset="utf-8">
<title>Dr. Rosalind Petrakis — Business Card</title>
<link href="https://fonts.googleapis.com/css2?family=Cinzel:wght@400;600&family=Montserrat:wght@400;500&display=swap" rel="stylesheet">
<style>
  :root {
    --backdrop: #d9d9db;
    --plum: #352c63;
    --plum-soft: #4a3f7d;
    --white: #ffffff;
    --ink: #3d3468;
    --muted: #5b5670;
    --gold: #f2a93b;
    --teal: #2fb3a4;
    --rose: #e0566c;
    --violet: #8b5cc4;
    --faint: #eeeef3;
  }
  * { margin: 0; padding: 0; box-sizing: border-box; }
  html, body { width: 900px; height: 1200px; overflow: hidden; }
  body { background: var(--backdrop); position: relative; font-family: "Montserrat", sans-serif; }

  .card {
    position: absolute; left: 153px; width: 594px; height: 345px;
    border-radius: 12px; overflow: hidden;
    box-shadow: 0 6px 16px rgba(0,0,0,0.18);
  }
  .card--back { top: 300px; background: var(--plum); color: var(--white); }
  .card--front { top: 675px; background: var(--white); color: var(--ink); }

  .mark-circle { position: absolute; border-radius: 50%; }
  .card--back .mark-circle { left: 36px; top: 24px; width: 96px; height: 96px; background: var(--white); }
  .card--front .mark-circle { left: 30px; top: 40px; width: 96px; height: 96px; background: var(--teal); }

  .decor-circle {
    position: absolute; right: -40px; width: 240px; height: 240px; border-radius: 50%;
  }
  .card--back .decor-circle { top: 20px; border: 2px solid rgba(255,255,255,0.07); }
  .card--front .decor-circle { top: 60px; border: 2px solid var(--faint); }

  .back-name { position: absolute; left: 150px; top: 20px; font-family: "Cinzel", serif; }
  .back-name .honorific { font-size: 20px; letter-spacing: 2px; display: flex; align-items: center; gap: 10px; }
  .back-name .honorific::after { content: ""; width: 150px; height: 1.5px; background: var(--white); }
  .back-name .full { font-size: 34px; line-height: 1.05; letter-spacing: 1px; font-weight: 600; }

  .specialties {
    position: absolute; left: 66px; top: 136px; list-style: none;
    display: grid; grid-template-columns: 210px 260px; column-gap: 16px; row-gap: 12px;
    font-size: 13.5px;
  }
  .specialties li { display: flex; align-items: center; gap: 8px; }
  .specialties svg { flex: none; }

  .front-rule { position: absolute; left: 150px; top: 36px; width: 3px; height: 130px; background: var(--gold); }
  .front-name { position: absolute; left: 170px; top: 40px; font-family: "Cinzel", serif; font-size: 25px; letter-spacing: 1px; color: var(--ink); }
  .front-title { position: absolute; left: 170px; top: 74px; font-size: 14px; color: var(--muted); }
  .contacts { position: absolute; left: 170px; top: 104px; list-style: none; font-size: 13px; color: var(--muted); }
  .contacts li { display: flex; align-items: center; gap: 8px; height: 21px; }
  .contacts .dot { width: 11px; height: 11px; border-radius: 50%; flex: none; }
  .dot--phone { background: var(--rose); }
  .dot--mail { background: var(--teal); }
  .dot--web { background: var(--violet); }
</style>
</head>
<body>
  <section class="card card--back" aria-label="Card back: specialties">
    <div class="decor-circle"></div>
    <div class="mark-circle"></div>
    <div class="back-name">
      <div class="honorific">DR.</div>
      <div class="full">ROSALIND<br>PETRAKIS</div>
    </div>
    <ul class="specialties">
      <li><svg width="14" height="14" viewBox="0 0 14 14"><circle cx="7" cy="7" r="6" fill="none" stroke="#fff" stroke-width="1.2"/><path d="M4 7.2l2 2 4-4.4" fill="none" stroke="#fff" stroke-width="1.4"/></svg>Stylistically Interesting</li>
      <li><svg width="14" height="14" viewBox="0 0 14 14"><circle cx="7" cy="7" r="6" fill="none" stroke="#fff" stroke-width="1.2"/><path d="M4 7.2l2 2 4-4.4" fill="none" stroke="#fff" stroke-width="1.4"/></svg>Gender Identity &amp; Sexual Orientation</li>
      <li><svg width="14" height="14" viewBox="0 0 14 14"><circle cx="7" cy="7" r="6" fill="none" stroke="#fff" stroke-width="1.2"/><path d="M4 7.2l2 2 4-4.4" fill="none" stroke="#fff" stroke-width="1.4"/></svg>Individual and Couples</li>
      <li><svg width="14" height="14" viewBox="0 0 14 14"><circle cx="7" cy="7" r="6" fill="none" stroke="#fff" stroke-width="1.2"/><path d="M4 7.2l2 2 4-4.4" fill="none" stroke="#fff" stroke-width="1.4"/></svg>Abuse and Trauma</li>
      <li><svg width="14" height="14" viewBox="0 0 14 14"><circle cx="7" cy="7" r="6" fill="none" stroke="#fff" stroke-width="1.2"/><path d="M4 7.2l2 2 4-4.4" fill="none" stroke="#fff" stroke-width="1.4"/></svg>Relationships and Infidelity</li>
      <li><svg width="14" height="14" viewBox="0 0 14 14"><circle cx="7" cy="7" r="6" fill="none" stroke="#fff" stroke-width="1.2"/><path d="M4 7.2l2 2 4-4.4" fill="none" stroke="#fff" stroke-width="1.4"/></svg>Sexual Compulsivity &amp; Addiction</li>
      <li><svg width="14" height="14" viewBox="0 0 14 14"><circle cx="7" cy="7" r="6" fill="none" stroke="#fff" stroke-width="1.2"/><path d="M4 7.2l2 2 4-4.4" fill="none" stroke="#fff" stroke-width="1.4"/></svg>Sexual Health &amp; Aging</li>
      <li><svg width="14" height="14" viewBox="0 0 14 14"><circle cx="7" cy="7" r="6" fill="none" stroke="#fff" stroke-width="1.2"/><path d="M4 7.2l2 2 4-4.4" fill="none" stroke="#fff" stroke-width="1.4"/></svg>Sexual Dysfunction</li>
    </ul>
  </section>

  <section class="card card--front" aria-label="Card front: name and contact">
    <div class="decor-circle"></div>
    <div class="mark-circle"></div>
    <div class="front-rule"></div>
    <h1 class="front-name">DR. ROSALIND PETRAKIS</h1>
    <p class="front-title">Licensed Psychologist</p>
    <ul class="contacts">
      <li><span class="dot dot--phone"></span>555.014.7788</li>
      <li><span class="dot dot--mail"></span>ros@drrospetrakis.example</li>
      <li><span class="dot dot--web"></span>drrospetrakis.example</li>
    </ul>
  </section>
</body>
</html>
```